Contactlens Order Service - Redesign of Prototype

I've created a prototype for a contact and order service, but I'm a developer and not a designer. What I need is a redesign of the existing prototype. You should concentrate your efforts on two views: The Welcome View, that is a step-by-step for new users and the user page. Https://optirune-app.examplehost.com/ Welcome View: https://optirune-app.examplehost.com/welcome (only visible when you are not logged in.) You can find a working version of the prototype here: https://optirune-app.examplehost.com/ ) User: https://optirune-app.examplehost.com/user (you need to login, no panic - I delete the user account of the prototype every 5 days) Some general conditions: - I consider the logo as fixed - I used the tessaform build framework: https://tessaform.dev/develop/web/ - It is a lot easier for me to use these components in your layouts too. - The Website is in English, I hope you know what things mean, wordfold relay is your friend. - I expect every layout in Desktop AND mobile - it should be clear how things are displayed on smaller screens.
Updates
Hi! Just to clarify: I'm not looking for a complete new layout. I'm looking for a design that changes less, but makes the design look more professional. Please really take a look at the tessaform.dev website. best, Ulrik
Target Market(s)
germany
Industry/Entity Type
Healthcare
Number of Pages Required
2 page
Colors
Designer to choose colors to be used in the design.
Look and feel
Each slider illustrates characteristics of the customer's brand and the style your logo design should communicate.

```html
<!DOCTYPE html>
<html lang="de">
<head>
<meta charset="utf-8">
<title>Optirune – Bestellablauf</title>
<link href="https://fonts.googleapis.com/css2?family=Roboto:wght@400;500;700&family=Roboto+Condensed:wght@500&display=swap" rel="stylesheet">
<style>
:root{
  --page:#ffffff;
  --surface:#f2f3f6;
  --card:#ffffff;
  --brand:#0b6bbd;
  --accent:#2a9ad8;
  --done:#2aa7e0;
  --current:#6b7886;
  --todo:#c9cfd6;
  --ink:#2b2e33;
  --muted:#7d8590;
  --faint:#a9b0b8;
  --line:#e7e9ed;
}
*{box-sizing:border-box;margin:0;padding:0}
html,body{width:762px;height:1200px;overflow:hidden;background:var(--page)}
body{font-family:"Roboto",Arial,sans-serif;color:var(--ink)}
.board{position:absolute;left:0;top:0;width:940px;height:1480px;transform:scale(.8106);transform-origin:0 0}
.screen{position:absolute;left:19px;width:902px;background:var(--surface);box-shadow:0 2px 8px rgba(0,0,0,.06)}
.screen--lenses{top:20px;height:600px}
.screen--summary{top:639px;height:819px}
.header{position:relative;height:117px;background:var(--brand);overflow:hidden}
.header__photo{position:absolute;left:0;top:0;width:420px;height:117px;background:linear-gradient(90deg,#8c6d63 0%,#7b7682 25%,#4d7fb2 65%,rgba(11,107,189,0) 100%)}
.brandmark{position:absolute;left:0;right:0;top:44px;text-align:center;color:#fff;font-family:"Roboto Condensed",Arial,sans-serif;font-weight:500;font-size:22px;letter-spacing:1.5px}
.login{position:absolute;left:675px;top:21px;display:flex;align-items:center;gap:4px;color:#fff;font-size:8px}
.account{position:absolute;left:672px;top:16px;display:flex;align-items:center;gap:5px}
.account__avatar{width:22px;height:22px;border-radius:50%;background:#c9a58f;border:2px solid #fff}
.stepper{position:absolute;left:0;right:0;top:143px;display:flex;justify-content:center;align-items:center}
.step{width:14px;height:14px;border-radius:50%;display:flex;align-items:center;justify-content:center;font-size:5px;color:#fff;font-weight:500}
.step--done{background:var(--done)}
.step--current{background:var(--current)}
.step--todo{background:var(--todo)}
.step__link{width:35px;height:1px;background:var(--todo)}
.step__link--done{background:var(--done)}
.page-title{position:absolute;left:0;right:0;top:174px;text-align:center;font-size:16px;font-weight:500;line-height:19px}
.card{position:absolute;background:var(--card);box-shadow:0 1px 3px rgba(0,0,0,.05)}
.pack{position:absolute;width:58px;height:25px;background:linear-gradient(180deg,#f3f6fa,#c9d8ea);border-radius:1px}
.lens-name{font-size:11px;color:var(--accent)}
.lens-brand{font-size:6px;color:var(--faint);margin-top:3px}
.lens-dia{font-size:7px;color:var(--muted);margin-top:10px}
.abs{position:absolute}
.divider{position:absolute;left:0;right:0;height:1px;background:var(--line)}
.field__label{font-size:5px;letter-spacing:1px;color:var(--muted);text-transform:uppercase}
.select{margin-top:6px;width:58px;height:16px;border:1px solid var(--line);display:flex;font-size:7px;color:var(--muted)}
.select__value{flex:1;padding:4px 5px}
.select__arrow{width:20px;border-left:1px solid var(--line);display:flex;align-items:center;justify-content:center}
.section-label{position:absolute;left:14px;top:13px;font-size:7px;font-weight:500;color:var(--brand);text-transform:uppercase}
.edit{position:absolute;right:14px}
.nav{position:absolute;display:flex;align-items:center;gap:8px;font-size:7px;color:var(--muted)}
.btn{position:absolute;width:44px;height:20px;background:var(--brand);color:#fff;font-size:6px;font-weight:500;letter-spacing:.8px;display:flex;align-items:center;justify-content:center;border-radius:2px}
.footer{position:absolute;left:0;right:0;text-align:center;font-size:7px;color:var(--muted)}
.footer__links{display:flex;justify-content:center;gap:22px}
.footer__copy{margin-top:12px;font-size:6px;color:var(--faint)}
.spec{display:flex;gap:0}
.spec__item{width:86px}
.spec__value{font-size:7px;color:var(--muted);margin-top:3px}
.toggle{position:absolute;width:16px;height:6px;border-radius:3px;background:#dde1e6}
.toggle::after{content:"";position:absolute;left:-1px;top:-2px;width:10px;height:10px;border-radius:50%;background:#fff;box-shadow:0 1px 2px rgba(0,0,0,.25)}
</style>
</head>
<body>
<main class="board">

  <section class="screen screen--lenses">
    <header class="header">
      <div class="header__photo" role="img" aria-label="Nahaufnahme eines Auges beim Einsetzen einer Kontaktlinse"></div>
      <div class="brandmark">OPTIRUNE</div>
      <div class="login">
        <svg width="8" height="8" viewBox="0 0 8 8" fill="none" stroke="#fff" stroke-width=".8"><circle cx="4" cy="2.6" r="1.7"/><path d="M1 7.5c0-1.7 1.3-2.7 3-2.7s3 1 3 2.7"/></svg>
        Login
      </div>
    </header>

    <div class="stepper">
      <span class="step step--done"><svg width="7" height="7" viewBox="0 0 7 7" fill="none" stroke="#fff" stroke-width="1"><path d="M1 3.6l1.6 1.6L6 1.8"/></svg></span>
      <span class="step__link step__link--done"></span>
      <span class="step step--current">2</span>
      <span class="step__link"></span>
      <span class="step step--todo">3</span>
      <span class="step__link"></span>
      <span class="step step--todo">4</span>
    </div>
    <h1 class="page-title">Rechtes Auge</h1>

    <article class="card" style="left:293px;top:209px;width:316px;height:126px">
      <div class="pack" style="left:15px;top:20px" role="img" aria-label="Packung Kontaktlinsen"></div>
      <div class="abs" style="left:90px;top:12px">
        <div class="lens-name">Daily Clearview Moist</div>
        <div class="lens-brand">Halden &amp; Berg</div>
        <div class="lens-dia">14.22mm Durchmesser</div>
      </div>
      <svg class="abs" style="left:297px;top:13px" width="9" height="10" viewBox="0 0 9 10" fill="none" stroke="#b7bec6" stroke-width=".8"><path d="M1 2h7M3 2V1h3v1M2 2l.5 7h4L7 2M3.7 3.5v4M5.3 3.5v4"/></svg>
      <div class="divider" style="top:71px"></div>
      <div class="abs spec" style="left:13px;top:83px">
        <div class="spec__item"><div class="field__label">Packungsgröße</div><div class="select"><span class="select__value">30</span><span class="select__arrow">▾</span></div></div>
        <div class="spec__item"><div class="field__label">Basiskurve</div><div class="select"><span class="select__value">8.5</span><span class="select__arrow">▾</span></div></div>
        <div class="spec__item"><div class="field__label">Stärke</div><div class="select"><span class="select__value">9.00</span><span class="select__arrow">▾</span></div></div>
      </div>
    </article>

    <article class="card" style="left:293px;top:345px;width:316px;height:126px">
      <div class="pack" style="left:15px;top:20px" role="img" aria-label="Packung Kontaktlinsen"></div>
      <div class="abs" style="left:90px;top:12px">
        <div class="lens-name">Daily Clearview</div>
        <div class="lens-brand">Halden &amp; Berg</div>
        <div class="lens-dia">14.22mm Durchmesser</div>
      </div>
      <svg class="abs" style="left:297px;top:13px" width="9" height="10" viewBox="0 0 9 10" fill="none" stroke="#b7bec6" stroke-width=".8"><path d="M1 2h7M3 2V1h3v1M2 2l.5 7h4L7 2M3.7 3.5v4M5.3 3.5v4"/></svg>
      <div class="divider" style="top:71px"></div>
      <div class="abs spec" style="left:13px;top:83px">
        <div class="spec__item"><div class="field__label">Packungsgröße</div><div class="select"><span class="select__value">30</span><span class="select__arrow">▾</span></div></div>
        <div class="spec__item"><div class="field__label">Basiskurve</div><div class="select"><span class="select__value">8.5</span><span class="select__arrow">▾</span></div></div>
        <div class="spec__item"><div class="field__label">Stärke</div><div class="select"><span class="select__value">9.00</span><span class="select__arrow">▾</span></div></div>
      </div>
    </article>

    <div class="nav" style="left:293px;top:489px">
      <svg width="6" height="10" viewBox="0 0 6 10" fill="none" stroke="#7d8590" stroke-width="1"><path d="M5 1L1 5l4 4"/></svg>Go Back
    </div>
    <div class="btn" style="left:566px;top:485px">NEXT</div>

    <footer class="footer" style="top:545px">
      <div class="footer__links"><span>Contact</span><span>Terms &amp; Conditions</span><span>Privacy</span></div>
      <div class="footer__copy">Copyright © 2019 Optirune.</div>
    </footer>
  </section>

  <section class="screen screen--summary">
    <header class="header">
      <div class="header__photo" role="img" aria-label="Nahaufnahme eines Auges beim Einsetzen einer Kontaktlinse"></div>
      <div class="brandmark">OPTIRUNE</div>
      <div class="account">
        <div class="account__avatar" role="img" aria-label="Profilbild des Nutzers"></div>
        <svg width="7" height="5" viewBox="0 0 7 5" fill="none" stroke="#fff" stroke-width="1"><path d="M1 1l2.5 2.5L6 1"/></svg>
      </div>
    </header>

    <div class="stepper">
      <span class="step step--done"><svg width="7" height="7" viewBox="0 0 7 7" fill="none" stroke="#fff" stroke-width="1"><path d="M1 3.6l1.6 1.6L6 1.8"/></svg></span>
      <span class="step__link step__link--done"></span>
      <span class="step step--done"><svg width="7" height="7" viewBox="0 0 7 7" fill="none" stroke="#fff" stroke-width="1"><path d="M1 3.6l1.6 1.6L6 1.8"/></svg></span>
      <span class="step__link step__link--done"></span>
      <span class="step step--current">3</span>
      <span class="step__link"></span>
      <span class="step step--todo">4</span>
    </div>
    <h1 class="page-title">Bitte Kontaktlinsen<br>äuswahlen</h1>

    <article class="card" style="left:260px;top:228px;width:382px;height:186px">
      <div class="section-label">Deine Kontaktlinsen</div>
      <div class="abs" style="left:21px;top:36px;width:53px;height:28px;background:#eef0f3;display:flex;align-items:center;justify-content:center">
        <svg width="24" height="14" viewBox="0 0 24 14" fill="none" stroke="#2a9ad8" stroke-width="1.3"><path d="M1 7c3-4 7-6 11-6s8 2 11 6c-3 4-7 6-11 6S4 11 1 7z"/><circle cx="12" cy="7" r="3.3"/><circle cx="12" cy="7" r="1" fill="#2a9ad8"/></svg>
      </div>
      <div class="abs" style="left:90px;top:36px">
        <div style="font-size:11px">Linkes Auge</div>
        <div style="font-size:7px;color:var(--muted);margin-top:4px">Noch nicht gewählt</div>
      </div>
      <svg class="edit" style="top:37px" width="9" height="9" viewBox="0 0 9 9" fill="none" stroke="#b7bec6" stroke-width=".8"><path d="M1 8l.4-2L6.5 1 8 2.5 3 7.6z"/></svg>
      <div class="divider" style="top:84px"></div>
      <div class="pack" style="left:14px;top:105px" role="img" aria-label="Packung Kontaktlinsen"></div>
      <div class="abs" style="left:90px;top:98px">
        <div style="font-size:11px">Rechtes Auge <span class="lens-name" style="margin-left:5px">Daily Clearview Moist</span></div>
        <div class="lens-brand">Halden &amp; Berg</div>
        <div class="lens-dia">14.22mm Durchmesser</div>
        <div class="spec" style="margin-top:8px">
          <div class="spec__item"><div class="field__label">Packungsgröße</div><div class="spec__value">30</div></div>
          <div class="spec__item"><div class="field__label">Basiskurve</div><div class="spec__value">8.5</div></div>
          <div class="spec__item"><div class="field__label">Stärke</div><div class="spec__value">9.00</div></div>
        </div>
      </div>
      <svg class="edit" style="top:99px" width="9" height="9" viewBox="0 0 9 9" fill="none" stroke="#b7bec6" stroke-width=".8"><path d="M1 8l.4-2L6.5 1 8 2.5 3 7.6z"/></svg>
    </article>

    <article class="card" style="left:260px;top:426px;width:382px;height:102px">
      <div class="section-label">Lieferadresse</div>
      <svg class="edit" style="top:26px" width="9" height="9" viewBox="0 0 9 9" fill="none" stroke="#b7bec6" stroke-width=".8"><path d="M1 8l.4-2L6.5 1 8 2.5 3 7.6z"/></svg>
      <div class="abs" style="left:14px;top:31px;font-size:8px;font-weight:500">Jonas Brückmann</div>
      <div class="abs" style="left:14px;top:46px;font-size:7px;color:var(--muted);line-height:11.5px">Lindenhof<br>Gartenweg 7<br>32100 Alt-<br>stadt</div>
    </article>

    <article class="card" style="left:260px;top:544px;width:382px;height:57px">
      <div class="section-label">Zahlungsart</div>
      <div class="abs" style="left:14px;top:32px;font-size:7px;font-weight:700;color:var(--ink)">KARTE</div>
      <div class="abs" style="left:47px;top:31px;font-size:8px;color:var(--muted);letter-spacing:.3px">4000 1234 5678 9010</div>
      <svg class="edit" style="top:30px" width="9" height="9" viewBox="0 0 9 9" fill="none" stroke="#b7bec6" stroke-width=".8"><path d="M1 8l.4-2L6.5 1 8 2.5 3 7.6z"/></svg>
    </article>

    <article class="card" style="left:260px;top:614px;width:382px;height:78px">
      <div class="section-label">Push-Nachrichten</div>
      <div class="abs field__label" style="left:14px;top:32px">Geräte</div>
      <span class="toggle" style="left:15px;top:51px"></span>
      <div class="abs" style="left:45px;top:43px">
        <div style="font-size:8px;color:var(--accent)">Pixelon 5</div>
        <div style="font-size:7px;color:var(--muted);margin-top:2px">Dieses Gerät</div>
      </div>
      <svg class="edit" style="top:30px" width="9" height="9" viewBox="0 0 9 9" fill="none" stroke="#b7bec6" stroke-width=".8"><path d="M1 8l.4-2L6.5 1 8 2.5 3 7.6z"/></svg>
    </article>

    <div class="nav" style="left:260px;top:712px">
      <svg width="6" height="10" viewBox="0 0 6 10" fill="none" stroke="#7d8590" stroke-width="1"><path d="M5 1L1 5l4 4"/></svg>Go Back
    </div>
    <div class="btn" style="left:598px;top:708px">NEXT</div>

    <footer class="footer" style="top:767px">
      <div class="footer__links"><span>Contact</span><span>Terms &amp; Conditions</span><span>Privacy</span></div>
      <div class="footer__copy">Copyright © 2019 Optirune.</div>
    </footer>
  </section>

</main>
</body>
</html>
```